Combining web page

We need a PSD webpage design for our PrestaShop store that shows food combining rules, you can see an example that we put here, you can follow the same information and food image combinations. You are just doing the design but the images when implemented on the website will be clickable that goes to product categories, all text and images will be editable.

This is just an example:
http://velmoraharvest.com/content/7-food-combining-rules

Target Market(s)

Natural Product and supplement industry

Industry/Entity Type

Store

Number of Pages Required

1 page

Colors

Designer to choose colors to be used in the design.

Requirements
Must have
• 1. Clear images.
• 2. Clear readable text.
• 3. Company name shown Velmora Harvest.
• 4. Follow the food rules as seen on the web page example, but not the same design.
• 5. Logo should be seen.
• 7. All text and images will be editable.
• 8. Make sure the food images are in their proper groups.
• 9. You are not coping the design we gave you but the details have to be the same, copy the text and the image food groups are important, you cannot just put any food in a group, and the combinations are important.
Nice to have
• Here is the website it is for http://velmoraharvest.com/

```html
<!DOCTYPE html>
<html lang="en">
<head>
<meta charset="utf-8">
<title>Velmora Harvest – Food Combining</title>
<link href="https://fonts.googleapis.com/css2?family=Raleway:wght@500;600;700;800&family=Open+Sans:wght@400;600;700&display=swap" rel="stylesheet">
<style>
:root{
  --red:#d51f26;
  --green:#4e920f;
  --green-light:#7bbd1e;
  --ink:#222;
  --muted:#777;
  --line:#e4e4e4;
  --band:#f4f4f4;
  --footer:#333333;
  --footer-deep:#2a2a2a;
  --chart-head:#f7c31c;
  --chart-a:#fcd649;
  --chart-b:#fde7a1;
  --chart-side:#c9874a;
  --tick:#4fa81c;
  --cross:#9a8f7a;
}
*{box-sizing:border-box;margin:0;padding:0}
html,body{width:1200px;height:2719px;overflow:hidden;background:#fff}
body{position:relative;font-family:"Open Sans",Arial,sans-serif;color:var(--ink)}
.abs{position:absolute}
h1,h2,h3,h4,.nav,.btn{font-family:Raleway,Arial,sans-serif}

/* top bar */
.topbar{top:0;left:0;width:1200px;height:33px;border-bottom:1px solid var(--line);font-size:11px}
.topbar .contact{left:172px;top:9px}
.topbar .contact b{font-weight:700}
.topbar .account{right:172px;top:0;height:33px;display:flex}
.topbar .account span{padding:0 16px;border-left:1px solid var(--line);line-height:33px;font-size:10.5px;font-weight:600;letter-spacing:.3px}

/* header */
.header{top:33px;left:0;width:1200px;height:76px}
.logo{display:flex;align-items:center;gap:8px;font-family:Raleway,Arial,sans-serif;font-weight:800;font-size:22px;color:var(--red)}
.logo i{width:14px;height:14px;background:var(--green);display:block}
.header .logo{left:172px;top:24px}
.nav{right:172px;top:30px;display:flex;gap:34px;font-size:11.5px;font-weight:700;letter-spacing:.8px;align-items:center}
.nav .cart{position:relative}
.nav .cart em{position:absolute;top:-7px;right:-7px;width:11px;height:11px;border-radius:50%;background:var(--red);color:#fff;font-size:7px;font-style:normal;text-align:center;line-height:11px}

/* hero */
.hero{top:109px;left:0;width:1200px;height:382px;background:
  radial-gradient(ellipse 260px 200px at 470px 240px,#f08a1c 0%,transparent 70%),
  radial-gradient(ellipse 220px 180px at 900px 130px,#f2b31e 0%,transparent 70%),
  radial-gradient(ellipse 240px 200px at 1080px 320px,#d42a1c 0%,transparent 70%),
  radial-gradient(ellipse 260px 220px at 120px 300px,#e8b41a 0%,transparent 70%),
  radial-gradient(ellipse 200px 160px at 140px 90px,#c9281a 0%,transparent 70%),
  linear-gradient(100deg,#c83a1a,#e3761c 40%,#e55a1a 70%,#c92a1c)}
.hero h1{position:absolute;top:113px;width:100%;text-align:center;color:#fff;font-size:36px;font-weight:800;letter-spacing:.5px}
.hero p{position:absolute;top:170px;width:100%;text-align:center;color:#fff;font-size:14px;line-height:27px}
.btn{display:inline-block;background:var(--red);color:#fff;font-weight:800;font-size:12.5px;letter-spacing:.6px;text-align:center}
.hero .btn{position:absolute;left:517px;top:250px;width:166px;height:34px;line-height:34px;border:1px solid #fff}

/* features */
.feature{top:553px;width:240px;text-align:center}
.feature .icon{width:72px;height:72px;border-radius:50%;background:var(--green);margin:0 auto;display:flex;align-items:center;justify-content:center}
.feature h3{margin-top:22px;font-size:12px;font-weight:800;letter-spacing:.6px}
.feature p{margin-top:5px;font-size:11px;line-height:20px;color:var(--muted)}

/* tabs */
.tabs{top:791px;left:172px;width:856px;height:27px;border-bottom:1px solid var(--line);display:flex;gap:0;padding-left:8px}
.tabs span{font-size:10.5px;padding:0 8px;line-height:26px;border:1px solid var(--line);border-bottom:none;background:#f7f7f7}
.tabs span.on{background:#fff;font-weight:600}

/* products */
.card{top:834px;width:198px}
.card .photo{height:241px;background:#f6f6f6;position:relative;display:flex;align-items:center;justify-content:center}
.card .fill{width:130px;height:110px;border-radius:50%}
.badge{position:absolute;top:5px;left:9px;font-size:10px;color:#fff;padding:0 9px;line-height:23px}
.badge.sale{background:var(--red)}
.badge.off{background:var(--green-light);left:5px}
.actions{position:absolute;left:0;bottom:0;width:100%;height:27px;display:flex;background:var(--green);color:#fff;font-size:10px}
.actions span{flex:1;text-align:center;line-height:27px}
.actions span+span{border-left:1px solid rgba(255,255,255,.45)}
.card h4{margin-top:18px;font-family:"Open Sans",Arial,sans-serif;font-weight:400;font-size:15px}
.price{margin-top:6px;font-size:12px}
.price s{color:#999;margin-right:6px}
.price b{color:var(--red);font-size:15px}

/* combine section */
.section-title{top:1212px;left:172px;width:856px;display:flex;align-items:center;gap:16px}
.section-title hr{flex:1;border:none;border-top:1px solid var(--line)}
.section-title h2{font-size:22px;font-weight:700;letter-spacing:.6px}
.bowl{top:1260px;left:572px}
.intro{top:1325px;left:272px;width:656px;text-align:center;font-size:11px;line-height:20px;color:#444}

.chart{top:1396px;left:172px;width:856px;border-collapse:collapse;table-layout:fixed}
.chart td,.chart th{height:34.5px;text-align:center;font-size:14px;border:1px solid rgba(255,255,255,.55)}
.chart th{background:var(--chart-head);font-size:12px;font-weight:700;height:33px}
.chart th.corner{background:var(--chart-side)}
.chart td.food{background:var(--chart-side);color:#fff;text-align:left;padding-left:9px;font-size:11px;font-weight:700;border-color:rgba(255,255,255,.7);border-left:none}
.chart td.num{background:var(--chart-side);color:#fff;font-size:12px;font-weight:700;border-left:none}
.chart tr:nth-child(odd) td{background:var(--chart-b)}
.chart tr:nth-child(even) td{background:var(--chart-a)}
.chart tr td.food,.chart tr td.num{background:var(--chart-side)}
.y{color:var(--tick)}
.n{color:var(--cross)}

/* promo */
.promo-img{top:1785px;left:172px;width:372px;height:245px;background:
  radial-gradient(ellipse 90px 70px at 90px 130px,#f2cf3a 0%,transparent 75%),
  radial-gradient(ellipse 70px 110px at 220px 110px,#d9b6c0 0%,transparent 75%),
  radial-gradient(ellipse 60px 40px at 300px 210px,#4a5a9a 0%,transparent 75%),
  #fff}
.promo h2{position:absolute;top:1831px;left:584px;font-size:22px;font-weight:800;letter-spacing:.4px}
.promo .sub{position:absolute;top:1871px;left:584px;width:440px;font-size:13.5px;line-height:20px;color:#888}
.promo .body{position:absolute;top:1944px;left:584px;width:440px;font-size:11px;line-height:20px;color:#333}
.promo .btn{position:absolute;top:2006px;left:584px;width:166px;height:35px;line-height:35px}

/* benefits band */
.band{top:2086px;left:0;width:1200px;height:154px;background:var(--band)}
.benefit{top:2134px;width:270px}
.benefit h4{display:flex;align-items:center;gap:10px;font-size:11.5px;font-weight:800;letter-spacing:.6px}
.benefit p{margin-top:10px;font-size:10px;line-height:20px;color:#888}

/* footer */
.footer{top:2240px;left:0;width:1200px;height:372px;background:var(--footer);color:#ddd}
.footer .col{position:absolute;top:62px}
.footer h5{font-family:Raleway,Arial,sans-serif;font-size:12px;font-weight:700;letter-spacing:1px;color:#eee;margin-bottom:14px}
.footer .logo{color:#fff;font-size:19px}
.footer .about{font-size:10px;line-height:17px;margin-top:18px}
.footer .about b{font-weight:700}
.footer ul{list-style:none;font-size:10px;line-height:22.5px}
.footer ul li::before{content:"›";margin-right:8px}
.post{width:190px;border-bottom:1px solid #4a4a4a;padding-bottom:12px;margin-bottom:14px}
.post p{font-size:11.5px;line-height:17px}
.post small{display:block;font-size:8.5px;color:#aaa;margin-top:4px;font-style:italic}
.newsletter{font-size:11.5px;line-height:18px}
.subscribe{display:flex;margin-top:16px;width:218px;height:26px}
.subscribe span{flex:1;background:#262626;font-size:9px;color:#888;line-height:26px;padding-left:36px}
.subscribe b{background:var(--green);color:#fff;font-size:10px;padding:0 10px;line-height:26px;font-weight:600}
.social{display:flex;gap:40px;margin-top:20px}
.social div{display:flex;align-items:center;gap:8px;font-size:8.5px;line-height:11px}
.social i{width:28px;height:28px;display:block}
.bottom{top:2612px;left:0;width:1200px;height:107px;background:var(--footer-deep);color:#888;font-size:9.5px;line-height:20px}
.bottom .copy{position:absolute;left:172px;top:28px}
.bottom .icons{position:absolute;right:172px;top:55px;display:flex;gap:14px}
.bottom .icons i{width:11px;height:11px;border-radius:50%;background:#777;display:block}
</style>
</head>
<body>

<div class="abs topbar">
  <div class="abs contact"><b>Call:</b> 1800-555-0147 | <b>Email:</b> info@velmoraharvest.com</div>
  <div class="abs account"><span>MY ACCOUNT</span><span>LOGIN</span></div>
</div>

<header class="abs header">
  <div class="abs logo"><i></i>Velmora Harvest</div>
  <nav class="abs nav">
    <span>PRODUCTS</span><span>INGREDIENTS</span><span>HEALTH CONCERNS</span><span>BLOG</span><span>MORE</span>
    <svg width="11" height="11" viewBox="0 0 12 12"><circle cx="5" cy="5" r="3.6" fill="none" stroke="#222" stroke-width="1.6"/><line x1="7.6" y1="7.6" x2="11" y2="11" stroke="#222" stroke-width="1.8"/></svg>
    <span class="cart"><svg width="13" height="12" viewBox="0 0 13 12"><path d="M0 1h2.5l1.8 7h6.5l1.5-5H3.5" fill="none" stroke="#222" stroke-width="1.4"/><circle cx="5" cy="10.5" r="1.1" fill="#222"/><circle cx="10" cy="10.5" r="1.1" fill="#222"/></svg><em>0</em></span>
  </nav>
</header>

<section class="abs hero" role="img" aria-label="Close-up photograph of fresh red, orange and yellow bell peppers">
  <h1>100% ORGANIC AND FRESH</h1>
  <p>Lorem ipsum dolor sit amet, consectetur adipiscing elit. Vestibulum non venenatis mauris.<br>Lsuscipit imperdiet facilisis.</p>
  <span class="btn">START SHOPPING</span>
</section>

<div class="abs feature" style="left:125px">
  <div class="icon"><svg width="38" height="38" viewBox="0 0 38 38" fill="none" stroke="#fff" stroke-width="2"><circle cx="14" cy="22" r="8"/><circle cx="25" cy="22" r="8"/><path d="M19 12c0-4 3-6 6-6"/></svg></div>
  <h3>GARDEN FRESH</h3><p>Food supliment made from<br>fresh garden product</p>
</div>
<div class="abs feature" style="left:355px">
  <div class="icon"><svg width="38" height="38" viewBox="0 0 38 38" fill="none" stroke="#fff" stroke-width="2"><path d="M19 34V8"/><path d="M19 14c-4-1-6-4-6-7 4 1 6 4 6 7zM19 14c4-1 6-4 6-7-4 1-6 4-6 7zM19 22c-4-1-6-4-6-7 4 1 6 4 6 7zM19 22c4-1 6-4 6-7-4 1-6 4-6 7z"/></svg></div>
  <h3>100% ORGANIC</h3><p>Organic product free from<br>harmful elements</p>
</div>
<div class="abs feature" style="left:600px">
  <div class="icon"><svg width="38" height="38" viewBox="0 0 38 38" fill="none" stroke="#fff" stroke-width="2"><path d="M19 32L7 20a7 7 0 0112-9 7 7 0 0112 9z"/><path d="M8 20h7l2-4 3 8 2-4h8"/></svg></div>
  <h3>BEST FOR HEALTH</h3><p>Best food combination for<br>beter health</p>
</div>
<div class="abs feature" style="left:835px">
  <div class="icon"><svg width="38" height="38" viewBox="0 0 38 38" fill="none" stroke="#fff" stroke-width="2"><path d="M9 29C9 15 17 8 30 8c0 13-7 21-21 21z"/><path d="M9 29L22 16"/></svg></div>
  <h3>NATURAL PRODUCT</h3><p>All products with natural<br>ingrediatents</p>
</div>

<div class="abs tabs"><span class="on">New Arrivals</span><span>Best Sellers</span><span>You may like</span></div>

<div class="abs card" style="left:172px">
  <div class="photo"><div class="fill" role="img" aria-label="Whole and halved lemons with leaves" style="background:radial-gradient(circle at 40% 45%,#f7d21c,#e9b80e 70%,#f6f6f6 72%)"></div>
    <span class="badge sale">Sale!</span>
    <div class="actions"><span>🛒︎ Add to Cart</span><span>⌕ Quick View</span></div></div>
  <h4>Organics Grapes</h4><div class="price"><s>$24.99</s><b>$12.49</b></div>
</div>
<div class="abs card" style="left:390px">
  <div class="photo"><div class="fill" role="img" aria-label="Red, green and orange bell peppers" style="background:linear-gradient(90deg,#d42a1c 0 33%,#3f8f1e 33% 66%,#f08a12 66%);border-radius:45%"></div></div>
  <h4>Organic Food</h4><div class="price"><s>$24.99</s><b>$12.49</b></div>
</div>
<div class="abs card" style="left:609px">
  <div class="photo"><div class="fill" role="img" aria-label="Three brown taro roots" style="background:radial-gradient(circle at 50% 50%,#8a6a4e,#6b4f38 70%,#f6f6f6 72%)"></div>
    <span class="badge off">50% Off*</span></div>
  <h4>Fresh Organic Food</h4><div class="price"><s>$24.99</s><b>$12.49</b></div>
</div>
<div class="abs card" style="left:828px">
  <div class="photo"><div class="fill" role="img" aria-label="Bunch of dark grapes with vine leaves" style="background:radial-gradient(circle at 40% 55%,#2f2d45,#3a3a5a 55%,#5c9e2a 70%,#f6f6f6 72%)"></div></div>
  <h4>Organic Food</h4><div class="price"><s>$24.99</s><b>$12.49</b></div>
</div>

<div class="abs section-title"><hr><h2>COMBINE YOUR FOOD FOR HEALTHY LIFE</h2><hr></div>
<svg class="abs bowl" width="56" height="50" viewBox="0 0 56 50" fill="none" stroke="#222" stroke-width="2"><path d="M4 22h48c0 12-10 20-24 20S4 34 4 22z"/><path d="M20 42v5h16v-5"/><circle cx="20" cy="14" r="6"/><circle cx="33" cy="12" r="7"/><path d="M42 20c0-6 4-10 8-12"/><path d="M10 30h36M14 36h28"/></svg>
<p class="abs intro">Lorem ipsum dolor sit amet, consectetur adipiscing elit.  Vero quod consequuntur quibusdam, enim expedita sed quia nesciunt incidunt accusamus necess  itatibus modi adipisci officia libero accusantium esse hic</p>

<table class="abs chart">
  <colgroup><col style="width:170px"><col style="width:24px"><col span="9"></colgroup>
  <tr><th class="corner" colspan="2"></th><th>1</th><th>2</th><th>3</th><th>4</th><th>5</th><th>6</th><th>7</th><th>8</th><th>9</th></tr>
  <tr><td class="food">CITRUS - acid foods</td><td class="num">1</td><td class="y">✓✓</td><td class="y">✓✓</td><td class="y">✓</td><td class="y">✓✓</td><td class="n">✕</td><td><span class="n">✕</span><span class="y">✓</span></td><td class="y">✓</td><td class="n">✕✕</td><td class="n">✕✕</td></tr>
  <tr><td class="food">FRUITS (Sub-acid)</td><td class="num">2</td><td class="y">✓✓</td><td class="y">✓✓</td><td class="y">✓✓</td><td class="y">✓✓</td><td class="n">✕</td><td><span class="n">✕</span><span class="y">✓</span></td><td class="y">✓</td><td class="n">✕✕</td><td class="n">✕✕</td></tr>
  <tr><td class="food">SWEET FRUITS (Palm)</td><td class="num">3</td><td class="y">✓</td><td class="y">✓✓</td><td class="y">✓✓</td><td class="y">✓✓</td><td class="y">✓✓</td><td class="n">✕✕</td><td><span class="n">✕</span><span class="y">✓</span></td><td class="n">✕</td><td class="n">✕✕</td></tr>
  <tr><td class="food">NEUTRAL FRUITS nuts, seeds</td><td class="num">4</td><td class="y">✓✓</td><td class="y">✓✓</td><td class="y">✓✓</td><td class="y">✓✓</td><td class="y">✓✓</td><td class="y">✓✓</td><td class="y">✓✓</td><td class="y">✓</td><td class="y">✓✓</td></tr>
  <tr><td class="food">GRAINS</td><td class="num">5</td><td class="n">✕</td><td class="n">✕</td><td class="y">✓✓</td><td class="y">✓✓</td><td class="y">✓✓</td><td class="y">✓✓</td><td><span class="n">✕</span><span class="y">✓</span></td><td class="y">✓✓</td><td class="y">✓✓</td></tr>
  <tr><td class="food">LEGUMES (dry) SPROUTS</td><td class="num">6</td><td><span class="n">✕</span><span class="y">✓</span></td><td><span class="n">✕</span><span class="y">✓</span></td><td class="n">✕✕</td><td class="y">✓✓</td><td class="y">✓✓</td><td class="y">✓✓</td><td class="y">✓✓</td><td class="y">✓✓</td><td class="y">✓✓</td></tr>
  <tr><td class="food">MELONS</td><td class="num">7</td><td class="y">✓</td><td class="y">✓</td><td class="n">✕</td><td class="y">✓</td><td><span class="n">✕</span><span class="y">✓</span></td><td class="n">✕</td><td class="y">✓✓</td><td class="n">✕</td><td class="n">✕</td></tr>
  <tr><td class="food">SUCCULENT FOOD (Tomatoes)</td><td class="num">8</td><td class="n">✕✕</td><td class="n">✕✕</td><td class="n">✕✕</td><td class="y">✓✓</td><td class="y">✓✓</td><td class="y">✓✓</td><td class="n">✕</td><td class="y">✓✓</td><td class="y">✓✓</td></tr>
  <tr><td class="food">VEGETABLES</td><td class="num">9</td><td class="n">✕✕</td><td class="n">✕✕</td><td class="n">✕✕</td><td class="y">✓✓</td><td class="y">✓✓</td><td class="y">✓✓</td><td class="n">✕</td><td class="y">✓✓</td><td class="y">✓✓</td></tr>
</table>

<div class="abs promo-img" role="img" aria-label="Bananas, a glass jug of berry smoothie, blueberries and seeds"></div>
<div class="promo">
  <h2>20% OFF ON COMBINED SUPPLIMENT*</h2>
  <p class="sub">Get the best food combination suppliment. Avail the offer with your cupon code</p>
  <p class="body">Lorem ipsum dolor sit amet, consectetur adipisicing elit. Eveniet cumque, perferendis accusamus porro illo exercitationem molestias.</p>
  <span class="btn">ORDER NOW</span>
</div>

<div class="abs band"></div>
<div class="abs benefit" style="left:172px">
  <h4><svg width="16" height="14" viewBox="0 0 16 14"><path d="M0 6h3v8H0zM4 6l4-6c2 0 2 2 1.5 4H15l-1 9H4z" fill="#222"/></svg>100% ORGINAL</h4>
  <p>Powerful Layout with Responsive functionality that can be adapted to any screen size.</p>
</div>
<div class="abs benefit" style="left:462px">
  <h4><svg width="18" height="13" viewBox="0 0 18 13"><rect x="0.5" y="0.5" width="17" height="12" rx="1.5" fill="none" stroke="#222"/><rect x="0" y="3" width="18" height="3" fill="#222"/></svg>PATMENT OPTIONS</h4>
  <p>Powerful Layout with Responsive functionality that can be adapted to any screen size.</p>
</div>
<div class="abs benefit" style="left:754px">
  <h4><svg width="19" height="13" viewBox="0 0 19 13"><path d="M0 1h11v8H0zM11 4h4l3 3v2h-7z" fill="#222"/><circle cx="4" cy="11" r="2" fill="#222"/><circle cx="14" cy="11" r="2" fill="#222"/></svg>FREE SHIPPING</h4>
  <p>Powerful Layout with Responsive functionality that can be adapted to any screen size.</p>
</div>

<footer class="abs footer">
  <div class="col" style="left:172px;top:56px">
    <div class="logo"><i></i>Velmora Harvest</div>
    <p class="about">We believe in Simple, Creative &amp;<br>Flexible Design Standards.<br><br><b>Headquarters:</b><br>218 Orchard Lane, Suite 40<br>Greenvale, CA 90000<br><br>Phone: (00) 55501 20480<br>Fax: (00) 5550 120481<br>Email: info@velmoraharvest.com</p>
  </div>
  <div class="col" style="left:386px">
    <h5>BLOGROLL</h5>
    <ul><li>Documentation</li><li>Feedback</li><li>Plugins</li><li>Support Forums</li><li>Themes</li><li>Pressleaf Blog</li><li>Pressleaf Planet</li></ul>
  </div>
  <div class="col" style="left:598px">
    <h5>RECENT POSTS</h5>
    <div class="post"><p>Lorem ipsum dolor sit amet, consectetur</p><small>20th July 2014</small></div>
    <div class="post"><p>Elit Assumenda vel amet dolorum quasi</p><small>20th July 2014</small></div>
    <div class="post" style="border:none"><p>Debitis nihil placeat, illum est nisi</p><small>20th July 2014</small></div>
  </div>
  <div class="col" style="left:810px">
    <p class="newsletter"><b>Subscribe</b> to Our Newsletter to get Important News, Amazing Offers &amp; Inside Scoops:</p>
    <div class="subscribe"><span>Enter Your Email</span><b>Subscribe</b></div>
    <div class="social">
      <div><i style="background:#3b5a96"></i>Like Us<br>on Facelink</div>
      <div><i style="background:#2aa3e0"></i>Follow us<br>on Chirper</div>
    </div>
  </div>
</footer>

<div class="abs bottom">
  <p class="copy">Copyrights © 2014 All Rights Reserved by velmoraharvest<br>Terms of Use / Privacy Policy</p>
  <div class="icons"><i></i><i></i><i></i><i></i><i></i><i></i><i></i></div>
</div>

</body>
</html>
```